Trade Show Banner "Calmwrightery"

1.7' x 3' vertical banner to complement trade show booth panels (3-panel tabletop booth attached). The word file (attached) is for text and not meant to imply design. We manage homeowner and condo associations that are run by volunteer boards of directors who already have full-time jobs or who may have no training in how to run an organization. It can be highly stressful and not very rewarding. We want this poster/banner to convey that feeling of stress along with a hope for relief and relaxation. Our logo is attached. The full logo is the top one in the file. You may also want to use the triangle (attached) in addition to or instead of the logo. Our corporate fonts are attached. Please let me know if you need additional information or if you feel like there is too much copy or any other thoughts or comments you have.

Target Market(s)

Volunteer boards of directors for homeowner and condo associations--all ages, genders, races, occupations.

Industry/Entity Type

Property Management

Other font styles liked:
• "Bright Harbor" is part of a trademark and should be in Mistral with the green from our logo

Requirements
Must have
• Simple, easy to read, don't clash with booth design
Nice to have
• convey the tension of stress contrasted with the feeling of relaxation and relief.

```html
<!DOCTYPE html>
<html lang="en">
<head>
<meta charset="utf-8">
<title>The Art of Calmwrightery for Board Members</title>
<link href="https://fonts.googleapis.com/css2?family=Source+Sans+3:wght@600;700&family=Lobster&family=Caveat:wght@600&display=swap" rel="stylesheet">
<style>
  :root {
    --backdrop: #434143;
    --paper: #ffffff;
    --wine: #7a1a1f;
    --navy: #2b2762;
    --leaf: #1d6d32;
    --rule: #c9c9d2;
    --sky: #dfe6ea;
    --sea: #9fb6c4;
    --sand: #eae7e1;
  }
  * { margin: 0; padding: 0; box-sizing: border-box; }
  html, body {
    width: 960px; height: 1200px; overflow: hidden;
    background: var(--backdrop);
    font-family: "Source Sans 3", Arial, sans-serif;
  }
  .banner {
    position: absolute; left: 184px; top: 78px;
    width: 592px; height: 1044px;
    background: var(--paper);
    overflow: hidden;
  }
  .hero-photo {
    position: absolute; left: 0; top: 0; width: 100%; height: 215px;
    background:
      linear-gradient(to bottom, rgba(255,255,255,0) 55%, var(--paper) 100%),
      linear-gradient(to bottom, var(--sky) 0%, #eef1f2 25%, var(--sea) 40%, #c5d3da 55%, var(--sand) 75%);
  }
  .headline { position: absolute; left: 0; width: 100%; text-align: center; }
  .headline-pre { top: 56px; font-size: 36px; font-weight: 700; color: var(--wine); }
  .headline-main {
    top: 98px; font-family: "Lobster", cursive; font-size: 64px; color: var(--leaf);
    -webkit-text-stroke: 2px #ffffff; paint-order: stroke fill;
    text-shadow: 2px 3px 4px rgba(0,0,0,0.35);
  }
  .headline-post { top: 182px; font-size: 33px; font-weight: 700; color: var(--wine); }

  .point { position: absolute; left: 30px; width: 532px; text-align: center; }
  .stress { font-size: 18.5px; font-weight: 700; color: var(--navy); line-height: 1; }
  .relief {
    margin-top: 14px; font-size: 18.5px; font-weight: 700; color: var(--wine); line-height: 1.25;
  }
  .relax-word { font-family: "Lobster", cursive; font-weight: 400; font-size: 23px; color: var(--leaf); }
  .trademark { font-family: "Caveat", cursive; font-size: 21px; color: var(--leaf); }
  .divider {
    position: absolute; left: 70px; width: 464px; height: 1px;
    background: linear-gradient(to right, rgba(201,201,210,0), var(--rule) 50%, rgba(201,201,210,0));
  }
  .cta {
    position: absolute; left: 25px; top: 858px; width: 542px; height: 37px;
    border-radius: 19px; background: var(--leaf); color: #fff;
    font-size: 20px; font-weight: 700; text-align: center; line-height: 37px;
  }
  .company {
    position: absolute; left: 0; width: 100%; top: 955px;
    display: flex; justify-content: center; align-items: center; gap: 10px;
    font-size: 19px; font-weight: 600; color: var(--wine); letter-spacing: 0.5px;
  }
  .company-mark { width: 16px; height: 16px; background: var(--navy); }
</style>
</head>
<body>
<main class="banner">
  <div class="hero-photo" role="img" aria-label="Beach scene with a businessman relaxing in a deck chair by the sea"></div>
  <p class="headline headline-pre">The Art of</p>
  <h1 class="headline headline-main">Calmwrightery</h1>
  <p class="headline headline-post">for Board Members</p>

  <section class="point" style="top:262px">
    <p class="stress">Stress: THE BOARD HAS TOO MUCH WORK TO DO</p>
    <p class="relief"><span class="relax-word">Relax</span>...and let us do the work.</p>
  </section>
  <div class="divider" style="top:336px"></div>

  <section class="point" style="top:361px">
    <p class="stress">Stress: YOUR COMMUNITY HAS “ISSUES”.</p>
    <p class="relief"><span class="relax-word">Relax</span>...and let us give you a <span class="trademark">Bright Harbor.</span></p>
  </section>
  <div class="divider" style="top:434px"></div>

  <section class="point" style="top:457px">
    <p class="stress">Stress: YOUR MEMBERS CANNOT PAY ONLINE.</p>
    <p class="relief"><span class="relax-word">Relax</span>...we’ll give your members multiple<br>ways to pay.</p>
  </section>
  <div class="divider" style="top:559px"></div>

  <section class="point" style="top:583px">
    <p class="stress">Stress: COMMUNICATION IS POOR OR INCONSISTENT.</p>
    <p class="relief"><span class="relax-word">Relax</span>...we’ll keep you informed with a robust<br>online portal, chock full of information.</p>
  </section>
  <div class="divider" style="top:682px"></div>

  <section class="point" style="top:700px">
    <p class="stress">Stress: YOUR DELINQUENCIES ARE HIGH.</p>
    <p class="relief"><span class="relax-word">Relax</span>...as a licensed collection agency, we have<br>developed an effective collections program that<br>works in tandem with your collections attorney.<br>Plus, we can report to the credit bureau!</p>
  </section>

  <p class="cta">COME IN TO TALK AND START RELAXING TODAY!</p>

  <div class="company">
    <span class="company-mark"></span>
    <span>NORTHVALE MANAGEMENT, INC.</span>
  </div>
</main>
</body>
</html>
```